Young, dynamic furniture company needs a new business card design

We require a new business card design for our modern furniture company which supplies furniture and appliances to the property and development market.
Thornvale Furnishing has become one of the leading furniture & appliance suppliers to the property market withing London. With over 10 years experience, we have increased our business to supply not only private landlords and managing agents, but also property developers, housing associations and local councils.
We offer not only a complete range of furniture which includes beds, wardrobes, dining sets and sofas, but also a high quality, full delivery and assembly service to help you with all our furnishing needs.

Target Market(s)

Private landlords, estate agents, letting agents, property management companies

Industry/Entity Type

Business

Contact Information for Business Card

Name,
Title,
Address,
Mobile,
Telephone,
Fax, Website, email address

Font styles to use
Sans Serif

Colors
3176b5
0555a3
85abd2
cfdeed

Requirements
Must have
• All the above information for each of our staff, along with our logo

```html
<!DOCTYPE html>
<html lang="en">
<head>
<meta charset="utf-8">
<title>Thornvale Furnishing – Business Card</title>
<link rel="stylesheet" href="https://fonts.googleapis.com/css2?family=Cabin:ital,wght@0,400;0,500;1,400&display=swap">
<style>
  :root {
    --page-bg: #eceef1;
    --navy: #1b2a52;
    --card-blue: #1d5494;
    --brand-light: #85abd2;
    --edge-light: #a9ccf0;
    --pale: #cfdeed;
    --white: #ffffff;
  }
  * { margin: 0; padding: 0; box-sizing: border-box; }
  html, body {
    width: 1200px;
    height: 1195px;
    overflow: hidden;
    background: var(--page-bg);
    font-family: "Cabin", sans-serif;
  }
  .canvas {
    position: relative;
    width: 1200px;
    height: 1195px;
  }

  /* Front of card */
  .card-front {
    position: absolute;
    left: 80px;
    top: 60px;
    width: 715px;
    height: 457px;
    background: var(--navy);
    border: 12px solid var(--edge-light);
    border-radius: 26px;
    display: flex;
    align-items: center;
    justify-content: center;
    gap: 28px;
  }
  .card-front .brand-square {
    width: 70px;
    height: 70px;
    flex: none;
    background: var(--brand-light);
  }
  .card-front .brand-name {
    font-size: 56px;
    font-weight: 500;
    color: var(--pale);
    letter-spacing: 0.5px;
    white-space: nowrap;
  }

  /* Back of card */
  .card-back {
    position: absolute;
    left: 347px;
    top: 637px;
    width: 719px;
    height: 461px;
    background: var(--card-blue);
    border-radius: 26px;
    color: var(--white);
  }
  .card-back .brand-name {
    position: absolute;
    left: 40px;
    top: 180px;
    width: 150px;
    font-size: 15px;
    font-weight: 500;
    line-height: 1.25;
    color: var(--white);
  }
  .contact-block {
    position: absolute;
    left: 206px;
    top: 46px;
  }
  .person-name {
    font-size: 25px;
    font-weight: 400;
    letter-spacing: 0.5px;
    line-height: 1.2;
  }
  .person-title {
    font-size: 17px;
    font-style: italic;
    color: var(--pale);
    margin-top: 2px;
  }
  .address {
    font-style: normal;
    font-size: 16px;
    line-height: 22.5px;
    margin-top: 28px;
  }
  .contact-lines {
    font-size: 16px;
    line-height: 24px;
    margin-top: 24px;
  }
  .contact-lines span + span { margin-left: 20px; }
</style>
</head>
<body>
  <main class="canvas">
    <section class="card-front" aria-label="Card front">
      <span class="brand-square"></span>
      <span class="brand-name">Thornvale Furnishing</span>
    </section>

    <section class="card-back" aria-label="Card back">
      <span class="brand-name">Thornvale Furnishing</span>
      <div class="contact-block">
        <h1 class="person-name">MR DANIEL REEVE</h1>
        <p class="person-title">GRAPHIC DESIGNER</p>
        <address class="address">
          Thornvale Furnishing - Trade<br>
          27B Hollow Lane Business Park<br>
          Eastmere<br>
          London<br>
          N24 5QR
        </address>
        <div class="contact-lines">
          <p><span>E daniel@thornvale.co.uk</span><span>T 020 7946 0321</span></p>
          <p><span>F 020 7946 0388</span><span>thornvale.co.uk</span></p>
        </div>
      </div>
    </section>
  </main>
</body>
</html>
```